buseisness card

design a card that similar to my web site
BRIXENTAPLORLLC .COM

Contact Information for Business Card

NAME PHONE # WEBSITE EMAIL AND DISCTIPTION OF WHAT WE DO

Colors
0054AA
0677BA
7BADD7
CADEEF
E8F1F8

Requirements
Must have
• lOGO AND DETAILS
Nice to have
• I LIKE THE WATER LIKE ON MY WEB SITE

```html
<!DOCTYPE html>
<html lang="en">
<head>
<meta charset="utf-8">
<title>Brixentaplor Business Card</title>
<link href="https://fonts.googleapis.com/css2?family=Montserrat:wght@400;500;700&family=Source+Sans+3:wght@400&display=swap" rel="stylesheet">
<style>
  :root {
    --navy: #2b3590;
    --deep: #1f4fa8;
    --cyan: #00aeef;
    --sky: #1ba7e4;
    --ink: #231f20;
    --paper: #ffffff;
    --page: #ffffff;
    --edge: #3a3a3a;
  }
  * { box-sizing: border-box; margin: 0; padding: 0; }
  html, body { width: 776px; height: 1200px; overflow: hidden; background: var(--page); }
  body { position: relative; font-family: "Montserrat", sans-serif; color: var(--ink); }

  .card {
    position: absolute; left: 48px; width: 680px; height: 389px;
    background: var(--paper); border: 1px solid var(--edge); overflow: hidden;
  }
  .card--front { top: 190px; }
  .card--back { top: 610px; }

  .water {
    position: absolute; left: 0; right: 0;
    background:
      radial-gradient(ellipse at 50% 55%, rgba(0,174,239,0.95) 0%, rgba(0,150,225,0.7) 35%, rgba(0,0,0,0) 70%),
      linear-gradient(180deg, var(--navy) 0%, var(--deep) 14%, #1c8fd6 32%, #0aa6e6 50%, #1873c6 74%, var(--navy) 100%);
  }
  .card--front .water { top: 0; height: 262px; }
  .card--back .water.band { bottom: 0; height: 74px;
    background: linear-gradient(180deg, #1f5fb5 0%, var(--navy) 100%); }

  .mark-dot {
    position: absolute; left: 50%; top: 70px; width: 66px; height: 66px;
    margin-left: -33px; border-radius: 50%; background: var(--paper);
  }
  .brand-name {
    position: absolute; left: 0; right: 0; top: 168px; text-align: center;
    font-family: "Montserrat", sans-serif; font-weight: 700; font-size: 42px;
    letter-spacing: 1px; color: var(--paper);
  }

  .service {
    position: absolute; left: 0; right: 0; top: 282px; text-align: center;
    font-family: "Source Sans 3", sans-serif; font-size: 27px; letter-spacing: 0.2px;
  }
  .accent { color: var(--sky); }
  .tagline {
    position: absolute; left: 0; right: 0; top: 322px; text-align: center;
    font-size: 15px; line-height: 20px;
  }

  .about {
    position: absolute; left: 40px; right: 40px; top: 62px; text-align: center;
    font-size: 17px; line-height: 23px;
  }
  .rule { position: absolute; left: 40px; width: 601px; top: 171px; height: 2px; background: var(--sky); }
  .col { position: absolute; top: 206px; font-size: 17px; }
  .col--contact { left: 40px; }
  .col--location { left: 370px; }
  .col h2 { font-weight: 400; font-size: 17px; margin-bottom: 20px; }
  .line { display: flex; align-items: center; gap: 10px; line-height: 22px; margin-bottom: 10px; }
  .line svg { flex: none; }
  .address { display: flex; gap: 16px; align-items: flex-start; line-height: 23px; }
  .address svg { margin-top: 10px; }
</style>
</head>
<body>
  <section class="card card--front">
    <div class="water" role="img" aria-label="Underwater photo of deep blue ocean with light rays"></div>
    <div class="mark-dot"></div>
    <div class="brand-name">BRIXENTAPLOR</div>
    <div class="service"><span class="accent">FOAM</span> PROPPORTIONER <span class="accent">TESTING</span></div>
    <div class="tagline">An <span class="accent">Eco</span> Friendly Company Doing<br><span class="accent">Eco</span> Friendly Testing</div>
  </section>

  <section class="card card--back">
    <p class="about">Proudly serving our community for over 20+ years. Leading technology in saving the enviornment and valued structures with foam proportioner testing.</p>
    <div class="rule"></div>
    <div class="col col--contact">
      <h2><span class="accent">contact</span> us</h2>
      <div class="line">
        <svg width="18" height="20" viewBox="0 0 24 24"><path fill="#231f20" d="M6.6 2.5 9.4 6.8c.4.6.3 1.3-.2 1.8L7.6 10c1.1 2.6 3.2 4.8 5.8 6l1.5-1.6c.5-.5 1.2-.6 1.8-.2l4.3 2.8c.6.4.8 1.2.4 1.8l-1.4 2.3c-.5.8-1.4 1.2-2.3 1C10 20.6 3.6 14.2 2.1 6.5c-.2-.9.2-1.8 1-2.3l1.8-1.2c.6-.4 1.3-.2 1.7.4z"/></svg>
        <span>+555 014 2283</span>
      </div>
      <div class="line">
        <svg width="22" height="16" viewBox="0 0 22 16"><rect x="0" y="0" width="22" height="16" fill="#231f20"/><path d="M1 1 11 9 21 1" fill="none" stroke="#fff" stroke-width="1.6"/></svg>
        <span>hello@brixentaplor.com</span>
      </div>
    </div>
    <div class="col col--location">
      <h2><span class="accent">Location</span></h2>
      <div class="address">
        <svg width="18" height="26" viewBox="0 0 18 26"><path fill="#231f20" d="M9 0C4 0 0 4 0 9c0 6 9 15 9 15s9-9 9-15c0-5-4-9-9-9zm0 13a4 4 0 1 1 0-8 4 4 0 0 1 0 8z"/><ellipse cx="9" cy="25" rx="5" ry="1" fill="#231f20"/></svg>
        <span>418 Harbor Line Drive<br>Lakeview, OH 40000</span>
      </div>
    </div>
    <div class="water band" role="img" aria-label="Strip of deep blue underwater photo"></div>
  </section>
</body>
</html>
```